Harbourline Strategy Group firm

I need a business card that is succint for a Brisbane based business called Harbourline Strategy Group Pty Ltd.
We bridge the gaps between People, Process and Technology.

We are a specialist operational excellence firm, delivering strategic consulting and business advisory services in six core capabilities, across all industries and all business lines to improve performance, efficiency, profitability, automation and scalability, for clients across Australia &New Zealand.
Updates

Hi Designers, I have uploaded the logo in 3D .png format, to assist in card design.

Target Market(s)

Project Management professionals, IT professionals, corporate and government clients managing transitioning or transformation projects.

Contact Information for Business Card

Harbourline Strategy Group Pty Ltd

Daniel Ferreira
Principal Consultant

mobile: +61 417 260 315
email: daniel@harbourlinestrategygroup.com.au
webpage: www.harbourlinestrategygroup.com

professional services: strategic advisors,

Font styles to use
Sans Serif

Requirements
Must have
• Business name: Harbourline Strategy Group
logo: attached
Contact person: Daniel Ferreira
Title: Principal Consultant
contact details:
mobile +61 417 260
email: daniel@HarbourlineStrategyGroup.com.au
website: HarbourlineStrategyGroup.com

on back side with logo include: A.B.N. 58210947362

professional services offered: Business Analysis, Strategic Advisory
Nice to have
• QR code
Should not have
• contacts picture

```html
<!DOCTYPE html>
<html lang="en">
<head>
<meta charset="utf-8">
<title>Harbourline Strategy Group – Business Card</title>
<link rel="stylesheet" href="https://fonts.googleapis.com/css2?family=Alegreya:wght@700&family=Roboto:wght@400;500&display=swap">
<style>
  :root {
    --backdrop: #777777;
    --paper: #ffffff;
    --navy: #212845;
    --red: #e32329;
    --ink: #2a2a2a;
  }
  * { margin: 0; padding: 0; box-sizing: border-box; }
  html, body { width: 1065px; height: 1200px; overflow: hidden; }
  body { background: var(--backdrop); position: relative; font-family: "Roboto", Arial, sans-serif; }

  .card { position: absolute; width: 583px; height: 363px; box-shadow: 2px 3px 3px rgba(0,0,0,0.75); }
  .card--front {
    left: 292px; top: 218px; background: var(--paper);
    border-radius: 0 181px 181px 0 / 0 181px 181px 0;
  }
  .card--back {
    left: 263px; top: 623px; background: var(--navy);
    border-radius: 181px 0 0 181px / 181px 0 0 181px;
  }

  .person { position: absolute; left: 30px; top: 43px; }
  .person__name {
    font-family: "Alegreya", Georgia, serif; font-weight: 700;
    font-size: 21px; letter-spacing: 0.3px; color: var(--navy); line-height: 1;
  }
  .person__name .first { color: var(--red); }
  .person__title { margin-top: 4px; font-size: 18px; color: var(--ink); }

  .brand { position: absolute; display: flex; align-items: center; gap: 14px; }
  .card--front .brand { left: 212px; top: 140px; }
  .card--back .brand { left: 129px; top: 141px; }
  .brand__mark { width: 36px; height: 36px; background: var(--red); flex: none; }
  .brand__name {
    font-family: "Roboto", Arial, sans-serif; font-weight: 500;
    font-size: 33px; line-height: 1.05; text-transform: uppercase; letter-spacing: 0.5px;
  }
  .card--front .brand__name { color: var(--navy); }
  .card--back .brand__name { color: var(--paper); }

  .contacts { position: absolute; left: 29px; top: 257px; list-style: none; }
  .contacts li {
    display: flex; align-items: center; height: 21.5px;
    font-size: 17px; color: var(--ink);
  }
  .contacts svg { width: 16px; height: 16px; margin-right: 6px; fill: var(--red); flex: none; }

  .tagline {
    position: absolute; left: 0; right: 0; top: 268px; text-align: center;
    font-family: "Alegreya", Georgia, serif; font-weight: 700;
    font-size: 15.5px; letter-spacing: 0.4px; color: var(--paper); text-transform: uppercase;
  }
  .tagline .lead { color: var(--red); }
</style>
</head>
<body>

<section class="card card--front">
  <div class="person">
    <p class="person__name"><span class="first">Daniel</span> Ferreira</p>
    <p class="person__title">Principal Consultant</p>
  </div>

  <div class="brand">
    <span class="brand__mark"></span>
    <p class="brand__name">Harbourline<br>Strategy Group</p>
  </div>

  <ul class="contacts">
    <li>
      <svg viewBox="0 0 24 24" aria-hidden="true"><path d="M6.6 10.8a15.1 15.1 0 0 0 6.6 6.6l2.2-2.2c.3-.3.7-.4 1-.2 1.1.4 2.3.6 3.6.6.6 0 1 .4 1 1V20c0 .6-.4 1-1 1C10.6 21 3 13.4 3 4c0-.6.4-1 1-1h3.5c.6 0 1 .4 1 1 0 1.3.2 2.5.6 3.6.1.3 0 .7-.2 1z"/><path d="M14 3a7 7 0 0 1 7 7h-2a5 5 0 0 0-5-5zm0 3a4 4 0 0 1 4 4h-2a2 2 0 0 0-2-2z"/></svg>
      +61 417 260 315
    </li>
    <li>
      <svg viewBox="0 0 24 24" aria-hidden="true"><path d="M2 5h20v14H2z M2 5l10 8 10-8" /><path d="M2 5h20L12 12.5z" fill="#fff" opacity="0.35"/></svg>
      daniel@harbourlinestrategygroup.com.au
    </li>
    <li>
      <svg viewBox="0 0 24 24" aria-hidden="true"><path d="M12 2a10 10 0 1 0 0 20 10 10 0 0 0 0-20zm7.9 9h-3.4a15 15 0 0 0-1.3-6.2A8 8 0 0 1 19.9 11zM12 4c.9 1.2 2.3 3.6 2.5 7h-5C9.7 7.6 11.1 5.2 12 4zM8.8 4.8A15 15 0 0 0 7.5 11H4.1a8 8 0 0 1 4.7-6.2zM4.1 13h3.4a15 15 0 0 0 1.3 6.2A8 8 0 0 1 4.1 13zM12 20c-.9-1.2-2.3-3.6-2.5-7h5c-.2 3.4-1.6 5.8-2.5 7zm3.2-.8a15 15 0 0 0 1.3-6.2h3.4a8 8 0 0 1-4.7 6.2z"/></svg>
      www.harbourlinestrategygroup.com
    </li>
  </ul>
</section>

<section class="card card--back">
  <div class="brand">
    <span class="brand__mark"></span>
    <p class="brand__name">Harbourline<br>Strategy Group</p>
  </div>
  <p class="tagline"><span class="lead">Professional Services:</span> Strategic Advisors</p>
</section>

</body>
</html>
```